Trifold Leaflet - Osteopathy

Trifold Leaflet (A4 size paper) to provide information and promote an established English seafront osteopathy clinic.
I would like a simple modern design to reflect the seafront location and the caring nature of osteopathy treatment. The design needs to be not be generic or too corporate.
At the top of the front page in a large font should be the word "Osteopathy" as it will be displayed in a rack of leaflets (photo attached) and needs to be eye-catching.
I have attached a logo file and some examples of the kinds of designs that I like- but i'm very open to your expert ideas!
Also attached is a photo of the location- a bit of an ugly building but right on the beach, it would be great if this location could be emphasized!
The Word files: Leaflets word-inside.doc & Leaflets word-outside.doc uploaded show the content that I'd like- this is definitely not set in stone and I appreciate that less content is probably needed. Feel free to include/leave out whatever you feel is right.
More info on the practice can be found on my website:
www.harrowdenbackcare.com
The shutterstock images are ones that I have previously bought the rights to use, but only use them if you think they suit you design- I have included them i case they are of use to you.
Target Market(s)
Any adult.
Industry/Entity Type
Building
Look and feel
Each slider illustrates characteristics of the customer's brand and the style your logo design should communicate.

```html
<!DOCTYPE html>
<html lang="en">
<head>
<meta charset="utf-8">
<title>Harrowden Osteopathy – Trifold Leaflet</title>
<link href="https://fonts.googleapis.com/css2?family=Arimo:ital,wght@0,400;0,700;1,400;1,700&display=swap" rel="stylesheet">
<style>
:root{
  --page:#d9d9db;
  --paper:#ffffff;
  --red:#b3161c;
  --blue-deep:#1c5e9c;
  --blue-mid:#2f86c4;
  --blue-light:#6cb8e4;
  --blue-pale:#a9d9f2;
  --ink-blue:#1f4f8f;
  --ink-grey:#3c3c3c;
  --dot:#f3e04a;
  --warm-1:#7a3f14;
  --warm-2:#d08a4a;
}
*{box-sizing:border-box;margin:0;padding:0}
html,body{width:1200px;height:900px;overflow:hidden}
body{background:var(--page);font-family:"Arimo",Arial,sans-serif;position:relative}
.leaflet{position:absolute;left:90px;top:190px;width:1020px;height:520px;display:flex;box-shadow:0 18px 40px rgba(0,0,0,.18)}
.panel{position:relative;width:340px;height:520px;background:var(--paper);overflow:hidden}
.panel + .panel{border-left:1px solid #e4e4e4}
.panel-bg{position:absolute;inset:0;width:100%;height:100%}
.soft-photo{position:absolute;left:0;top:80px;width:340px;height:260px;background:radial-gradient(ellipse at 55% 50%,#eef3f8 0%,#dfe8f1 55%,rgba(255,255,255,0) 80%)}
.brand{position:absolute;font-weight:400;color:var(--red);font-size:19px;white-space:nowrap}
.brand-mark{display:inline-block;width:10px;height:10px;border-radius:50%;background:var(--red);margin-right:7px;vertical-align:middle}

/* left panel */
.bio-name{position:absolute;left:22px;top:76px;color:var(--red);font-weight:700;font-size:11px}
.bio-cred{position:absolute;left:22px;top:90px;color:var(--ink-blue);font-size:9px;font-weight:700}
.portrait{position:absolute;left:150px;top:60px;width:84px;height:92px;background:linear-gradient(#e9e4de,#c9c2b9);border:3px solid #fff;box-shadow:0 1px 3px rgba(0,0,0,.3)}
.bio-text{position:absolute;left:22px;top:160px;width:290px;color:var(--ink-blue);font-size:9.5px;line-height:1.35}
.bio-text p+p{margin-top:6px}
.booking{position:absolute;left:28px;top:262px;width:280px;height:56px;border-radius:16px;background:var(--blue-deep);color:#fff;font-weight:700;font-size:10.5px;line-height:1.4;text-align:center;padding:7px 12px}
.visit{position:absolute;left:28px;top:330px;color:var(--red);font-weight:700;font-size:12px}

/* middle panel */
.middle .brand{left:50%;transform:translateX(-50%);top:150px}
.venue-photo{position:absolute;left:30px;top:190px;width:280px;height:52px;background:linear-gradient(#a9c7e6 0%,#cfdeee 45%,#b9a99b 75%,#8f8579 100%);border:2px solid #fff;box-shadow:0 1px 3px rgba(0,0,0,.25)}
.venue{position:absolute;left:30px;top:246px;width:280px;height:92px;background:rgba(255,255,255,.82);text-align:center;padding-top:8px}
.venue-name{color:var(--red);font-weight:700;font-style:italic;font-size:13px}
.venue-line{color:var(--ink-grey);font-weight:700;font-style:italic;font-size:12px;line-height:1.25}
.venue-small{font-size:9.5px}
.tel{position:absolute;left:0;width:100%;top:418px;text-align:center;color:#fff;font-weight:700;font-style:italic;font-size:19px;letter-spacing:.5px}
.web{position:absolute;left:0;width:100%;top:452px;text-align:center;color:#fff;font-weight:700;font-size:13px;letter-spacing:.3px}

/* right panel */
.right .brand{left:30px;top:48px}
.treatment-photo{position:absolute;left:0;top:96px;width:340px;height:230px;background:linear-gradient(110deg,var(--warm-1) 0%,#9a5624 45%,var(--warm-2) 100%)}
.benefits{position:absolute;left:22px;top:118px;color:#fff;font-weight:700;font-size:11.5px;line-height:1.35;font-variant:small-caps;letter-spacing:.6px}
.headline{position:absolute;left:22px;top:186px;color:#fff;font-weight:700;font-size:26px;line-height:1.2}
.services{position:absolute;left:26px;top:348px;list-style:none;color:#fff;font-weight:700;font-size:10.5px;line-height:1.7}
.services li{position:relative;padding-left:16px}
.services li::before{content:"";position:absolute;left:0;top:5px;width:8px;height:8px;border-radius:50%;background:var(--dot)}
.address{position:absolute;left:0;width:100%;top:462px;text-align:center;color:#fff;font-weight:700;font-size:12px;line-height:1.3}
</style>
</head>
<body>
<main class="leaflet">

  <!-- inside panel: practitioner -->
  <section class="panel left">
    <div class="soft-photo" role="img" aria-label="Faint photo of hands treating a patient's shoulder"></div>
    <svg class="panel-bg" viewBox="0 0 340 520" aria-hidden="true">
      <path d="M0 52 Q170 90 340 58 L340 70 Q170 104 0 66Z" fill="var(--red)"/>
      <path d="M0 300 Q120 240 340 268 L340 520 L0 520Z" fill="var(--blue-light)" opacity=".55"/>
      <path d="M0 330 Q150 270 340 300 L340 520 L0 520Z" fill="var(--blue-mid)"/>
      <path d="M0 420 Q170 380 340 410 L340 520 L0 520Z" fill="var(--blue-deep)" opacity=".55"/>
      <rect x="0" y="470" width="340" height="50" fill="var(--blue-pale)" opacity=".8"/>
    </svg>
    <div class="portrait" role="img" aria-label="Portrait photo of the osteopath"></div>
    <h2 class="bio-name">Martin Ellery</h2>
    <p class="bio-cred">BSc (Hons)</p>
    <div class="bio-text">
      <p>Martin Ellery is an experienced osteopath who treats back, neck and joint pain with gentle hands-on care. He works with patients of all ages and offers tailored exercise advice for long-term recovery.</p>
      <p><strong>Martin</strong> is registered with the national osteopathic council and trained in modern techniques for shoulder rehabilitation.</p>
    </div>
    <p class="booking">For further information, or to book an appointment, please call the Shoreline Fitness Centre</p>
    <p class="visit">visit: www.harrowdenbackcare.com</p>
  </section>

  <!-- back panel: location -->
  <section class="panel middle">
    <div class="soft-photo" role="img" aria-label="Faint photo of hands on a patient's back"></div>
    <svg class="panel-bg" viewBox="0 0 340 520" aria-hidden="true">
      <path d="M0 62 Q170 30 340 60 L340 72 Q170 44 0 76Z" fill="var(--red)"/>
      <path d="M0 360 Q170 320 340 350 L340 520 L0 520Z" fill="var(--blue-light)" opacity=".6"/>
      <path d="M0 385 Q170 350 340 370 L340 520 L0 520Z" fill="var(--blue-mid)"/>
      <rect x="0" y="480" width="340" height="40" fill="var(--blue-pale)" opacity=".85"/>
    </svg>
    <p class="brand"><span class="brand-mark"></span>Harrowden Osteopathy</p>
    <div class="venue-photo" role="img" aria-label="Photo of the seafront clinic building by the beach"></div>
    <div class="venue">
      <p class="venue-name">The Shoreline Fitness Centre</p>
      <p class="venue-line">Seafront, Marine Parade,</p>
      <p class="venue-line venue-small">(next to the Old Fort)</p>
      <p class="venue-line">Harrowden HN4 7QD</p>
    </div>
    <p class="tel">Tel: 01632 960 417</p>
    <p class="web">www.harrowdenbackcare.com</p>
  </section>

  <!-- front cover -->
  <section class="panel right">
    <div class="treatment-photo" role="img" aria-label="Warm-toned photo of a massage treatment with hands on a back"></div>
    <svg class="panel-bg" viewBox="0 0 340 520" aria-hidden="true">
      <path d="M0 96 Q200 100 340 50 L340 62 Q200 112 0 108Z" fill="var(--red)"/>
      <path d="M0 310 Q170 270 340 300 L340 520 L0 520Z" fill="var(--blue-light)" opacity=".7"/>
      <path d="M0 330 Q170 300 340 318 L340 520 L0 520Z" fill="var(--blue-mid)"/>
      <path d="M0 450 Q170 420 340 440 L340 520 L0 520Z" fill="var(--blue-light)" opacity=".7"/>
    </svg>
    <p class="brand"><span class="brand-mark"></span>Harrowden Osteopathy</p>
    <p class="benefits">Natural Fitness<br>Relaxation<br>Pain Relief</p>
    <h1 class="headline">Feel Better and<br>Enjoy Life</h1>
    <ul class="services">
      <li>Regulated and safe OSTEOPATHY</li>
      <li>SHORT-TERM PAIN RELIEF</li>
      <li>FROZEN SHOULDER</li>
      <li>CRANIAL OSTEOPATHY</li>
      <li>PATIENT SATISFACTION</li>
    </ul>
    <p class="address">Shoreline Fitness Centre, Marine Parade<br>HARROWDEN, HN4 7QD</p>
  </section>

</main>
</body>
</html>
```